Marrow Business Cards

Front of business card will have logo, name, address, & telephone number. Back of card will have a list of services provided - Roads, Substation Pads, Temporary Pads, Site Pads, Land Leveling, Powerline Row Cleaning, Land Clearing, Gates, Fencing, Construction Entrances, Excavation, Trenching, Underground Utilities, Directional Boring, Pile Driving. We are a construction company that uses heavy equipment like bulldozers, motor graders/blades, dump trucks, backhoes, hydro axes, & skid loaders. We build roads, pads, & install electric utility lines & waterlines underground. This logo is new. The word "Construction" can be smaller as uploaded 2 example edited logos. We will be using this card design for many employees.
Target Market(s)
Industrial Electric Powerline, Wind Turbine, Solar Panel, & Water Utility companies.
Contact Information for Business Card
Name/Position - Dorian Quale - Owner
Address: 4837 FM 582
Calder, TX 79418
Phone number - (325) 418-2906

```html
<!DOCTYPE html>
<html lang="en">
<head>
<meta charset="utf-8">
<title>Marrow Construction Business Cards</title>
<link rel="stylesheet" href="https://fonts.googleapis.com/css2?family=Marcellus&family=Montserrat:wght@400;700;800&display=swap">
<style>
  :root {
    --backdrop: #1d1d1f;
    --card: #3d131c;
    --ink: #ffffff;
    --edge: #f4f0f0;
  }
  * { box-sizing: border-box; margin: 0; padding: 0; }
  html, body { width: 1200px; height: 900px; overflow: hidden; }
  body {
    background: var(--backdrop);
    font-family: "Montserrat", Arial, sans-serif;
    color: var(--ink);
  }
  .canvas {
    position: relative;
    width: 1200px;
    height: 900px;
  }
  .card {
    position: absolute;
    left: 270px;
    width: 660px;
    height: 377px;
    background: var(--card);
    border: 3px solid var(--edge);
    box-shadow: 0 10px 30px rgba(0,0,0,.55);
    overflow: hidden;
  }
  .card--back { top: 55px; }
  .card--front { top: 468px; }

  .brand { text-align: center; }
  .brand__name {
    font-family: "Montserrat", Arial, sans-serif;
    font-weight: 800;
    letter-spacing: 2px;
    line-height: 1;
  }
  .brand__tag {
    font-family: "Marcellus", Georgia, serif;
    letter-spacing: 1px;
    line-height: 1;
  }
  .card--back .brand {
    position: absolute;
    left: 0; right: 0; top: 108px;
  }
  .card--back .brand__name { font-size: 74px; }
  .card--back .brand__tag { font-size: 34px; margin-top: 26px; }

  .card--front .brand {
    position: absolute;
    left: 36px; top: 132px; width: 240px;
  }
  .card--front .brand__name { font-size: 44px; letter-spacing: 1px; }
  .card--front .brand__tag { font-size: 22px; margin-top: 22px; }
  .divider {
    position: absolute;
    left: 298px; top: 110px;
    width: 2px; height: 158px;
    background: var(--ink);
  }
  .contact {
    position: absolute;
    left: 326px; top: 128px;
    width: 310px;
  }
  .contact__name {
    font-weight: 700;
    font-size: 31px;
    letter-spacing: 2px;
    text-transform: uppercase;
    line-height: 1;
    white-space: nowrap;
  }
  .contact__role {
    font-weight: 700;
    font-size: 11px;
    letter-spacing: 1.5px;
    text-transform: uppercase;
    margin-top: 4px;
  }
  .contact__list { list-style: none; margin-top: 18px; }
  .contact__item {
    display: flex;
    align-items: center;
    gap: 10px;
    font-size: 18px;
    margin-bottom: 8px;
    white-space: nowrap;
  }
  .contact__icon { width: 17px; height: 17px; flex: none; }
</style>
</head>
<body>
<main class="canvas">

  <section class="card card--back" aria-label="Card back">
    <div class="brand">
      <div class="brand__name">MARROW</div>
      <div class="brand__tag">CONSTRUCTION</div>
    </div>
  </section>

  <section class="card card--front" aria-label="Card front">
    <div class="brand">
      <div class="brand__name">MARROW</div>
      <div class="brand__tag">CONSTRUCTION</div>
    </div>
    <div class="divider"></div>
    <div class="contact">
      <div class="contact__name">Dorian Quale</div>
      <div class="contact__role">Owner</div>
      <ul class="contact__list">
        <li class="contact__item">
          <svg class="contact__icon" viewBox="0 0 24 24" fill="none" stroke="#fff" stroke-width="2" stroke-linecap="round" stroke-linejoin="round" aria-hidden="true">
            <circle cx="12" cy="12" r="10"/>
            <path d="M8.5 7.5c.5-.5 1.3-.5 1.7 0l1 1.4c.3.4.2 1-.1 1.3l-.6.6c.5 1.2 1.5 2.2 2.7 2.7l.6-.6c.4-.3.9-.4 1.3-.1l1.4 1c.5.4.5 1.2 0 1.7l-.6.6c-.8.8-2 .9-3 .4-2.3-1.2-4.1-3-5.3-5.3-.5-1-.4-2.2.4-3z"/>
          </svg>
          <span>(325) 418-2906</span>
        </li>
        <li class="contact__item">
          <svg class="contact__icon" viewBox="0 0 24 24" fill="none" stroke="#fff" stroke-width="2" stroke-linecap="round" stroke-linejoin="round" aria-hidden="true">
            <path d="M12 22s7-6.5 7-12a7 7 0 0 0-14 0c0 5.5 7 12 7 12z"/>
            <circle cx="12" cy="10" r="2.5"/>
          </svg>
          <span>4837 FM 582, Calder, TX 79418</span>
        </li>
      </ul>
    </div>
  </section>

</main>
</body>
</html>
```